Client Referral Scheme

To design a brochure to advertise our client referral scheme.
Referees will be estate agents, architects, builders, tradesmen etc.
Front page: Tidewell Interiors Ltd with logo
Title: Client referral scheme
Quality German kitchens designed & installed
website address: www.tidewellinteriors.im
white background, black, grey, yellow theme as per logo
Centre pages: How the scheme works (see attachment), pictures of kitchens from brandor kitchens
Back page: info about us from our website

" attachments below are my ideas, however I want them to be far classier as per the Pemberly interiors brochure

Industry/Entity Type

Builders

Requirements
Must have
• The refer mid document attached must be the middle page

```html
<!DOCTYPE html>
<html lang="en">
<head>
<meta charset="utf-8">
<title>Tidewell Interiors – Client Referral Scheme</title>
<link href="https://fonts.googleapis.com/css2?family=Lato:ital,wght@0,400;0,700;0,900;1,400&family=Roboto+Condensed:wght@400;700&display=swap" rel="stylesheet">
<style>
  :root {
    --yellow: #f2c400;
    --charcoal: #2e2e2e;
    --grey: #6b6b6b;
    --light-grey: #d8d8d8;
    --stage: #e4e4e4;
    --white: #ffffff;
  }
  * { box-sizing: border-box; margin: 0; padding: 0; }
  html, body { width: 1200px; height: 1200px; overflow: hidden; }
  body {
    background: var(--stage);
    font-family: "Lato", Arial, sans-serif;
    color: var(--charcoal);
    position: relative;
  }
  .spread {
    position: absolute;
    top: 232px;
    left: 70px;
    display: flex;
    gap: 20px;
  }
  .page {
    width: 520px;
    height: 736px;
    background: var(--white);
    position: relative;
    overflow: hidden;
    box-shadow: 0 6px 18px rgba(0,0,0,0.18);
  }

  /* Back page */
  .back-copy { padding: 46px 40px 0 40px; }
  .section-title {
    color: var(--yellow);
    font-weight: 700;
    font-size: 17px;
    letter-spacing: 0.5px;
    margin-bottom: 6px;
  }
  .section-text { font-size: 11.5px; line-height: 1.45; }
  .rule { height: 3px; background: var(--yellow); margin: 20px 0 22px; }
  .contact {
    position: absolute;
    top: 370px; left: 0; right: 0; height: 190px;
    background: linear-gradient(180deg, #fafafa 0%, #eeeeee 100%);
    padding: 36px 40px 0;
  }
  .contact-grid { display: flex; gap: 30px; }
  .contact-col { font-size: 12.5px; line-height: 1.55; }
  .contact-col.divided { border-left: 3px solid var(--yellow); padding-left: 14px; height: 44px; }
  .contact-line { display: flex; align-items: center; gap: 7px; }
  .contact-line svg { flex: none; }
  .socials { display: flex; gap: 16px; margin-top: 16px; }
  .social-dot { width: 30px; height: 30px; border-radius: 50%; background: var(--yellow); }
  .back-band {
    position: absolute; left: 0; right: 0; bottom: 0; height: 176px;
    background: var(--charcoal);
    display: flex; align-items: center; padding-left: 40px;
  }
  .brand { display: flex; align-items: center; gap: 10px; }
  .brand-dot { width: 26px; height: 26px; border-radius: 50%; border: 3px solid currentColor; flex: none; }
  .brand-name { font-weight: 900; font-size: 22px; white-space: nowrap; }
  .brand.on-dark { color: var(--white); }
  .brand-tagline { font-size: 10px; color: #999; margin-top: 3px; margin-left: 36px; white-space: nowrap; }

  /* Front page */
  .front-head { padding: 44px 0 0; text-align: center; }
  .front-head .brand { justify-content: center; color: var(--grey); }
  .front-head .brand-name { font-size: 26px; }
  .front-head .brand-tagline { margin-left: 70px; color: #8a8a8a; }
  .front-rule { height: 3px; background: var(--yellow); margin-top: 18px; }
  .hero {
    height: 200px;
    background: linear-gradient(160deg, #9a9a96 0%, #c9c2b4 45%, #6a6660 100%);
  }
  .thumbs {
    display: flex; justify-content: center; gap: 10px;
    margin-top: -28px; position: relative;
  }
  .thumb {
    width: 156px; height: 86px;
    border: 3px solid var(--yellow);
    border-radius: 6px;
    box-shadow: 0 0 0 3px var(--white);
  }
  .thumb.one { background: linear-gradient(135deg, #4a5a3a, #8a6a48); }
  .thumb.two { background: linear-gradient(135deg, #bfb8aa, #6a5a48); }
  .thumb.three { background: linear-gradient(135deg, #7a7570, #3e3b38); }
  .title {
    font-family: "Roboto Condensed", "Arial Narrow", sans-serif;
    font-weight: 700;
    font-size: 42px;
    text-align: center;
    margin-top: 48px;
    letter-spacing: 0.5px;
    white-space: nowrap;
  }
  .title .accent { color: var(--yellow); }
  .subtitle {
    font-family: "Roboto Condensed", "Arial Narrow", sans-serif;
    font-size: 26px;
    color: var(--grey);
    text-align: center;
    margin-top: 2px;
    white-space: nowrap;
  }
  .web-button {
    display: block; width: 300px; margin: 34px auto 0;
    background: var(--charcoal); color: var(--yellow);
    font-weight: 700; font-size: 16px; text-align: center;
    padding: 10px 0;
  }
  .front-foot { position: absolute; left: 0; right: 0; bottom: 0; height: 60px; }
</style>
</head>
<body>
  <main class="spread">
    <section class="page back-page">
      <div class="back-copy">
        <h2 class="section-title">OUR HISTORY</h2>
        <p class="section-text">The company is lead by Managing Director Martin Quayle, who is an experienced and highly-qualified Carpenter and Joiner. He will work with you every step of the way in creating your dream room. Martin's kitchen installation success led him to take a keen interest in the design of a kitchen and its components. He saw first-hand the repeated flaws many kitchen designers would make in not completely understanding the dynamics of a kitchen area. An installer has to understand every aspect of a kitchen or bedroom. This includes electrics, gas, plumbing, plastering, tiling and much more. An experienced fitter knows what can and can't be fitted in different spaces.</p>
        <div class="rule"></div>
        <h2 class="section-title">OUR PHILOSOPHY</h2>
        <p class="section-text">The best form of advertising we use is maintaining a level of quality and service that cannot be questioned. This ensures that each of our clients come away with the satisfaction that their needs and requirements were met in such a way that they can't help but tell people who we are and what we did.</p>
      </div>
      <div class="contact">
        <div class="contact-grid">
          <div class="contact-col">
            <h2 class="section-title">CONTACT US</h2>
            <div class="contact-line">
              <svg width="10" height="13" viewBox="0 0 10 13"><path d="M5 0a5 5 0 0 0-5 5c0 3.5 5 8 5 8s5-4.5 5-8a5 5 0 0 0-5-5zm0 7a2 2 0 1 1 0-4 2 2 0 0 1 0 4z" fill="#2e2e2e"/></svg>
              <span>Unit 4, Harbour Row, Kirkmore,<br>Isle of Man, IM9 3QT.</span>
            </div>
            <div class="contact-line">
              <svg width="11" height="11" viewBox="0 0 12 12"><circle cx="6" cy="6" r="5" fill="none" stroke="#2e2e2e" stroke-width="1.5"/><path d="M1 6h10M6 1c2 2 2 8 0 10M6 1c-2 2-2 8 0 10" fill="none" stroke="#2e2e2e"/></svg>
              <span>www.tidewellinteriors.im</span>
            </div>
            <div class="socials">
              <span class="social-dot"></span><span class="social-dot"></span><span class="social-dot"></span>
            </div>
          </div>
          <div class="contact-col divided">
            <div class="contact-line">
              <svg width="12" height="9" viewBox="0 0 12 9"><rect x="0.5" y="0.5" width="11" height="8" fill="none" stroke="#2e2e2e"/><path d="M0.5 0.5l5.5 4.5 5.5-4.5" fill="none" stroke="#2e2e2e"/></svg>
              <span>info@tidewellinteriors.im</span>
            </div>
            <div class="contact-line">
              <svg width="11" height="11" viewBox="0 0 12 12"><path d="M2.5 0.5l2 2.5-1.2 1.5a7 7 0 0 0 4.2 4.2l1.5-1.2 2.5 2-1.5 2C5 11 1 7 0.5 2z" fill="#2e2e2e"/></svg>
              <span>(01624) 555210</span>
            </div>
          </div>
        </div>
      </div>
      <div class="back-band">
        <div>
          <div class="brand on-dark"><span class="brand-dot"></span><span class="brand-name">Tidewell Interiors</span></div>
          <div class="brand-tagline">"kitchens built around you"</div>
        </div>
      </div>
    </section>

    <section class="page front-page">
      <header class="front-head">
        <div class="brand"><span class="brand-dot"></span><span class="brand-name">Tidewell Interiors</span></div>
        <div class="brand-tagline">"kitchens built around you"</div>
        <div class="front-rule"></div>
      </header>
      <div class="hero" role="img" aria-label="Photograph of a modern fitted kitchen with island and bar stools"></div>
      <div class="thumbs">
        <div class="thumb one" role="img" aria-label="Kitchen photograph with wooden dining table"></div>
        <div class="thumb two" role="img" aria-label="Kitchen photograph with wood-finish island"></div>
        <div class="thumb three" role="img" aria-label="Kitchen photograph in a stone-walled loft"></div>
      </div>
      <h1 class="title"><span class="accent">CLIENT</span> REFERRAL <span class="accent">SCHEME</span></h1>
      <p class="subtitle">Quality German kitchens designed &amp; installed</p>
      <span class="web-button">www.tidewellinteriors.im</span>
      <svg class="front-foot" width="520" height="60" viewBox="0 0 520 60" preserveAspectRatio="none">
        <path d="M0 40 Q260 20 520 14 L520 60 L0 60 Z" fill="#ffffff"/>
        <path d="M0 40 Q260 20 520 14" fill="none" stroke="#f2c400" stroke-width="5"/>
      </svg>
    </section>
  </main>
</body>
</html>
```